Dravolith Business Card

I have a logo that I would like to use to design the Business Card for Dravolith Construction LLC. We are a commercial general contractor in San Antonio Texas. Id like a simple and sleek design. Message me if you have any questions. Thanks

Industry/Entity Type

Contractor

```html
<!DOCTYPE html>
<html lang="en">
<head>
<meta charset="utf-8">
<title>Dravolith Business Card</title>
<link href="https://fonts.googleapis.com/css2?family=Oswald:wght@400;600&family=Roboto:wght@400&display=swap" rel="stylesheet">
<style>
  :root{
    --page:#e6e2dc;
    --card-white:#ffffff;
    --brand-blue:#3c6db6;
    --ink:#2a2a2a;
    --on-blue:#ffffff;
    --map-tone:#eeeeee;
  }
  *{box-sizing:border-box;margin:0;padding:0}
  html,body{width:1200px;height:970px;overflow:hidden;background:var(--page)}
  .canvas{position:relative;width:1200px;height:970px}
  .card{position:absolute;left:250px;width:700px;height:400px;background:var(--card-white);overflow:hidden;box-shadow:0 6px 18px rgba(0,0,0,.18)}
  .card--front{top:60px}
  .card--back{top:510px}
  .band{position:absolute;left:0;top:0;width:700px;height:400px}
  .map-area{position:absolute;left:250px;top:0;width:450px;height:185px;background:radial-gradient(ellipse at 60% 45%,#e4e4e4,var(--map-tone) 70%,#fff)}
  .wordmark{position:absolute;left:70px;top:78px;display:flex;align-items:center;gap:14px;font-family:'Oswald',sans-serif;font-weight:600;color:var(--ink);text-transform:uppercase;line-height:.95}
  .wordmark__square{width:46px;height:46px;background:var(--brand-blue)}
  .wordmark__name{font-size:40px;letter-spacing:1px}
  .wordmark__sub{display:block;font-size:24px;letter-spacing:1px}
  .website{position:absolute;left:0;right:0;top:290px;text-align:center;font-family:'Roboto',sans-serif;font-size:18px;letter-spacing:6px;color:var(--on-blue)}
  .person{position:absolute;left:70px;top:250px;color:var(--on-blue);font-family:'Oswald',sans-serif}
  .person__name{font-size:44px;font-weight:600;letter-spacing:1px;text-transform:uppercase;line-height:1}
  .person__title{font-size:15px;letter-spacing:2px;text-transform:uppercase;margin-top:4px}
  .contacts{position:absolute;left:390px;top:232px;display:grid;grid-template-columns:auto auto;gap:12px 22px;font-family:'Roboto',sans-serif;font-size:12.5px;color:var(--on-blue)}
  .contact{display:flex;align-items:center;gap:7px;white-space:nowrap}
  .contact--wide{grid-column:1 / span 2}
  .contact svg{width:18px;height:18px;flex:none}
</style>
</head>
<body>
<div class="canvas">

  <section class="card card--front" aria-label="Card front">
    <svg class="band" viewBox="0 0 700 400" aria-hidden="true">
      <polygon points="0,185 200,185 215,200 230,185 700,185 700,400 0,400" fill="var(--brand-blue)"/>
    </svg>
    <div class="wordmark">
      <span class="wordmark__square"></span>
      <span><span class="wordmark__name">Dravolith</span><span class="wordmark__sub">Construction LLC</span></span>
    </div>
    <p class="website">www.dravolithbuild.com</p>
  </section>

  <section class="card card--back" aria-label="Card back">
    <div class="map-area" role="img" aria-label="Faint world map in the background"></div>
    <svg class="band" viewBox="0 0 700 400" aria-hidden="true">
      <polygon points="0,185 200,185 215,200 230,185 700,185 700,400 0,400" fill="var(--brand-blue)"/>
    </svg>
    <div class="wordmark">
      <span class="wordmark__square"></span>
      <span><span class="wordmark__name">Dravolith</span><span class="wordmark__sub">Construction LLC</span></span>
    </div>
    <div class="person">
      <p class="person__name">Marcus Hale</p>
      <p class="person__title">General Manager</p>
    </div>
    <div class="contacts">
      <p class="contact">
        <svg viewBox="0 0 18 18" aria-hidden="true"><circle cx="9" cy="9" r="8" fill="none" stroke="#fff" stroke-width="1.2"/><path d="M6 5l2 2-1 1.2c.6 1.3 1.5 2.2 2.8 2.8L11 10l2 2-1.2 1.2C8.5 12.8 5.2 9.5 4.8 6.2z" fill="#fff"/></svg>
        210 555 0147
      </p>
      <p class="contact">
        <svg viewBox="0 0 18 18" aria-hidden="true"><circle cx="9" cy="9" r="8" fill="none" stroke="#fff" stroke-width="1.2"/><rect x="5" y="6" width="8" height="6" fill="none" stroke="#fff"/><path d="M5 6l4 3.5L13 6" fill="none" stroke="#fff"/></svg>
        info@dravolith.com
      </p>
      <p class="contact">
        <svg viewBox="0 0 18 18" aria-hidden="true"><circle cx="9" cy="9" r="8" fill="none" stroke="#fff" stroke-width="1.2"/><rect x="6.5" y="4.5" width="5" height="9" rx="1" fill="none" stroke="#fff"/></svg>
        210 555 0148
      </p>
      <p class="contact">
        <svg viewBox="0 0 18 18" aria-hidden="true"><circle cx="9" cy="9" r="8" fill="none" stroke="#fff" stroke-width="1.2"/><circle cx="9" cy="9" r="4.5" fill="none" stroke="#fff"/><path d="M4.5 9h9M9 4.5v9" stroke="#fff"/></svg>
        www.dravolithbuild.com
      </p>
      <p class="contact contact--wide">
        <svg viewBox="0 0 18 18" aria-hidden="true"><circle cx="9" cy="9" r="8" fill="none" stroke="#fff" stroke-width="1.2"/><path d="M9 13.5s-3-3.2-3-5.5a3 3 0 016 0c0 2.3-3 5.5-3 5.5z" fill="#fff"/></svg>
        4200 Bandera Road, Suite 3W
      </p>
    </div>
  </section>

</div>
</body>
</html>
```